Need high-end luxury business cards with raised element of logo

Looking for a non-standard business card with the option of part of our logo elements to be printed as raised or embossed. Would like at least 5 different photos on the backside. Looking at printing through this: https://www.cardvelo.com/raised-spot-uv-business-cards.html

updated the logo file

```html
<!DOCTYPE html>
<html lang="en">
<head>
<meta charset="utf-8">
<title>Highcrest Lodge — Business Card</title>
<link href="https://fonts.googleapis.com/css2?family=Montserrat:wght@400;500;700;800&display=swap" rel="stylesheet">
<style>
  :root{
    --slate:#3e5f75;
    --slate-dark:#2f4a5c;
    --paper:#ffffff;
    --stage:#e6e8ea;
    --ink:#3b5a6f;
  }
  *{box-sizing:border-box;margin:0;padding:0}
  html,body{width:1200px;height:1015px;overflow:hidden;background:var(--stage)}
  body{font-family:"Montserrat",Arial,sans-serif;color:var(--ink)}
  .card{position:absolute;left:220px;width:760px;height:434px;overflow:hidden;box-shadow:0 6px 18px rgba(0,0,0,.18)}
  .card--front{top:44px;background:var(--slate)}
  .card--back{top:537px;background:var(--paper)}

  .photo{position:absolute;border:5px solid var(--paper)}
  .photo--forest{left:-5px;top:88px;width:258px;height:262px;
    background:linear-gradient(160deg,#b9c6d4 0%,#c98a3a 28%,#b5561f 55%,#6f7f3a 80%,#8a8f86 100%)}
  .photo--interior{left:252px;top:-5px;width:252px;height:232px;
    background:radial-gradient(circle at 42% 55%,#f6a13a 0%,#b35a1f 22%,#6b3416 55%,#3a1e10 100%)}
  .photo--hottub{left:208px;top:192px;width:266px;height:247px;
    background:linear-gradient(180deg,#8f86a8 0%,#6d5b59 38%,#2fb8b5 62%,#1f8e94 85%,#2b3336 100%)}
  .photo--porch{left:468px;top:68px;width:297px;height:276px;
    background:linear-gradient(165deg,#e7924a 0%,#b9642c 30%,#7a3b1d 60%,#c9b8a4 100%)}

  .front-brand{position:absolute;left:0;top:350px;width:208px;height:84px;
    display:flex;flex-direction:column;align-items:center;justify-content:center;color:var(--paper)}
  .front-brand .brand-name{font-weight:500;font-size:21px;letter-spacing:4px}
  .front-brand .brand-sub{font-weight:500;font-size:9px;letter-spacing:5px;margin-top:3px}

  .back-accent{position:absolute;left:0;top:258px;width:44px;height:44px;background:var(--slate)}
  .person{position:absolute;left:92px;top:238px}
  .person-name{font-weight:800;font-size:25px;letter-spacing:.5px;color:var(--slate)}
  .person-role{font-weight:400;font-size:13px;letter-spacing:1px;margin-top:2px}

  .contact{position:absolute;left:92px;top:312px;list-style:none;font-size:15px}
  .contact li{display:flex;align-items:center;gap:9px;height:24px}
  .contact svg{width:16px;height:16px;flex:none}

  .address{position:absolute;left:92px;top:388px;font-size:14px;line-height:1.3}

  .back-brand{position:absolute;left:410px;top:112px;width:320px;text-align:center;color:var(--slate)}
  .back-brand .brand-name{font-weight:500;font-size:40px;letter-spacing:8px}
  .back-brand .brand-rule{display:flex;align-items:center;gap:12px;justify-content:center;margin-top:6px}
  .back-brand .brand-rule span{display:block;width:80px;height:1.5px;background:var(--slate)}
  .back-brand .brand-sub{font-weight:500;font-size:13px;letter-spacing:7px}
</style>
</head>
<body>

<section class="card card--front" aria-label="Card front">
  <div class="photo photo--forest" role="img" aria-label="Aerial photo of an autumn forest hillside with a lodge"></div>
  <div class="photo photo--interior" role="img" aria-label="Photo of a wooden cabin interior with stone fireplace"></div>
  <div class="photo photo--hottub" role="img" aria-label="Photo of a lit hot tub on a covered deck at dusk"></div>
  <div class="photo photo--porch" role="img" aria-label="Photo of a porch overlooking autumn mountains at sunset"></div>
  <div class="front-brand">
    <div class="brand-name">HIGHCREST</div>
    <div class="brand-sub">LODGE</div>
  </div>
</section>

<section class="card card--back" aria-label="Card back">
  <div class="back-brand">
    <div class="brand-name">HIGHCREST</div>
    <div class="brand-rule"><span></span><div class="brand-sub">LODGE</div><span></span></div>
  </div>

  <div class="back-accent"></div>
  <div class="person">
    <div class="person-name">DANIEL MARLOW</div>
    <div class="person-role">MANAGING DIRECTOR</div>
  </div>

  <ul class="contact">
    <li><svg viewBox="0 0 16 16"><path d="M4 1.5l2.5 3-1.5 1.8c.8 1.8 2.2 3.2 4 4l1.8-1.5 3 2.5-1.6 2.2C8 13.2 2.8 8 1.9 3.1z" fill="var(--ink)"/></svg>044-555 010 274</li>
    <li><svg viewBox="0 0 16 16"><rect x="1" y="3" width="14" height="10" fill="var(--ink)"/><path d="M1 3l7 5.5L15 3" fill="none" stroke="#fff" stroke-width="1.2"/></svg>hello@highcrestlodge.com</li>
    <li><svg viewBox="0 0 16 16" fill="none" stroke="var(--ink)" stroke-width="1.3"><circle cx="8" cy="8" r="6.5"/><ellipse cx="8" cy="8" rx="3" ry="6.5"/><path d="M1.5 8h13M2.5 5h11M2.5 11h11"/></svg>www.highcrestlodge.com</li>
  </ul>

  <address class="address" style="font-style:normal">218, Ridgeview Road<br>28711, Blue Valley</address>
</section>

</body>
</html>
```